Financial website header

We need a graphic/image for financial website to pump it up a bit and make it more stand out of crowd.

I would like to replace that image with dollar symbols...image is attached.

Industry/Entity Type

Financial

Requirements
Must have
• - Keep money/stock market symbolics
- Match current color design and fonts
Nice to have
• Maybe some background graph as symbolics for stock rise? Or some dollar coins?

```html
<!DOCTYPE html>
<html lang="en">
<head>
<meta charset="utf-8">
<title>Summit Ledger Reports</title>
<link href="https://fonts.googleapis.com/css2?family=Oswald:wght@300;400;500;700&family=Lato:wght@300;400&display=swap" rel="stylesheet">
<style>
  :root {
    --page-bg: #f3f1f0;
    --column-bg: #f3f0ef;
    --brand-blue: #0a7cc9;
    --link-blue: #1b87c9;
    --band-blue-light: #1aa3e2;
    --band-blue-dark: #0b6fba;
    --ink-dark: #2a2a2a;
    --ink-body: #5e5e5e;
    --ink-muted: #9a9a9a;
    --accent-red: #d9414e;
    --box-bg: #f9f8f8;
  }
  * { box-sizing: border-box; margin: 0; padding: 0; }
  html, body { width: 1178px; height: 1200px; overflow: hidden; background: var(--page-bg); }
  body { position: relative; font-family: 'Lato', sans-serif; }

  .site-column {
    position: absolute; left: 143px; top: 0; width: 890px; height: 1200px;
    background: var(--column-bg);
    box-shadow: -2px 0 3px rgba(0,0,0,.18), 2px 0 3px rgba(0,0,0,.18);
  }

  .brand { position: absolute; left: 180px; top: 30px; color: var(--brand-blue); font-family: 'Oswald', sans-serif; font-weight: 500; line-height: 1; }
  .brand-line { display: block; font-size: 68px; letter-spacing: 1px; }
  .brand-line + .brand-line { margin-top: 4px; }

  .main-nav { position: absolute; right: 165px; top: 83px; display: flex; align-items: center; gap: 10px; font-family: 'Oswald', sans-serif; font-weight: 300; font-size: 14px; color: var(--link-blue); }
  .main-nav .sep { color: var(--link-blue); margin: 0 2px; }
  .main-nav svg { display: block; }

  .hero-banner {
    position: absolute; left: 141px; top: 205px; width: 890px; height: 328px;
    background: radial-gradient(ellipse at 60% 40%, #f2f2f4 0%, #c9cacf 55%, #8d8f96 100%);
    box-shadow: 0 2px 6px rgba(0,0,0,.35);
  }

  .intro-title { position: absolute; left: 167px; top: 560px; font-family: 'Oswald', sans-serif; font-weight: 300; font-size: 40px; color: var(--ink-dark); }
  .intro-title strong { font-weight: 700; }
  .intro-text { position: absolute; left: 167px; top: 622px; font-size: 14px; font-weight: 300; color: var(--ink-body); }

  .btn-red { background: var(--accent-red); color: #fff; font-family: 'Oswald', sans-serif; font-weight: 400; border: 1px solid #b92c39; }
  .signup-button { position: absolute; left: 167px; top: 680px; width: 200px; height: 35px; font-size: 13px; display: flex; align-items: center; justify-content: center; }

  .signup-form { position: absolute; left: 601px; top: 663px; }
  .signup-form label { display: block; font-size: 14px; color: var(--ink-body); margin-bottom: 5px; }
  .email-field { position: absolute; left: 0; top: 21px; width: 328px; height: 29px; background: #fff; border: 1px solid #e2e0df; }
  .subscribe-button { position: absolute; left: 334px; top: 25px; width: 64px; height: 25px; font-size: 12px; display: flex; align-items: center; justify-content: center; }

  .featured-band {
    position: absolute; left: 144px; top: 776px; width: 665px; height: 46px;
    background: linear-gradient(180deg, var(--band-blue-light), var(--band-blue-dark));
    display: flex; align-items: center; padding-left: 22px; gap: 8px;
    font-family: 'Oswald', sans-serif; font-weight: 300; font-size: 36px; color: #1c2630;
  }

  .report-title { position: absolute; left: 167px; top: 840px; font-family: 'Oswald', sans-serif; font-weight: 300; font-size: 38px; color: var(--link-blue); }

  .report-body { position: absolute; left: 167px; top: 917px; width: 622px; font-size: 14.5px; line-height: 23.2px; font-weight: 300; color: var(--ink-body); }
  .report-body p + p { margin-top: 35px; padding-left: 15px; }

  .side-nav { position: absolute; left: 831px; width: 176px; list-style: none; }
  .side-nav li { height: 36px; margin-bottom: 4.5px; background: var(--box-bg); display: flex; align-items: center; font-size: 14.5px; }
  .side-nav.topics { top: 776px; }
  .side-nav.topics li { color: var(--ink-muted); padding-left: 14px; }
  .side-nav.legal { top: 916px; }
  .side-nav.legal li { color: var(--link-blue); padding-left: 17px; }
</style>
</head>
<body>
  <div class="site-column"></div>

  <div class="brand">
    <span class="brand-line">SUMMIT LEDGER</span>
    <span class="brand-line">REPORTS</span>
  </div>

  <nav class="main-nav">
    <svg width="22" height="16" viewBox="0 0 22 16" aria-hidden="true">
      <g stroke="#9a9a9a" stroke-width="1.4"><line x1="0" y1="2" x2="22" y2="2"/><line x1="0" y1="6" x2="22" y2="6"/><line x1="0" y1="10" x2="22" y2="10"/><line x1="0" y1="14" x2="16" y2="14"/></g>
    </svg>
    <span>Home</span><span class="sep">/</span>
    <span>About Us</span><span class="sep">/</span>
    <span>Latest Reports</span><span class="sep">/</span>
    <span>Disclaimer</span>
    <svg width="18" height="18" viewBox="0 0 18 18" aria-hidden="true">
      <circle cx="7" cy="7" r="5" fill="none" stroke="#9a9a9a" stroke-width="2"/>
      <line x1="11" y1="11" x2="17" y2="17" stroke="#9a9a9a" stroke-width="2.4"/>
    </svg>
  </nav>

  <div class="hero-banner" role="img" aria-label="Banner illustration: a money tree on a stage beside a figure in a tie, city skyline, with the headline Let us shine the light on serious stock profit potential"></div>

  <h1 class="intro-title"><strong>Profit</strong> Potential</h1>
  <p class="intro-text">Let Us Shine a Light on Serious Stock Profit Potential! Dont wait, sign up.</p>

  <div class="signup-button btn-red">Sign up for free stock analysis reports</div>

  <div class="signup-form">
    <label>Free sign-up, please enter your email:</label>
    <div class="email-field"></div>
    <div class="subscribe-button btn-red">Subscribe</div>
  </div>

  <div class="featured-band">
    <svg width="32" height="30" viewBox="0 0 32 30" aria-hidden="true">
      <path d="M16 2c-1.5 0-2.5 1-2.5 2.3C8.5 5.5 7 10 7 14v6l-4 4v1h26v-1l-4-4v-6c0-4-1.5-8.5-6.5-9.7C18.5 3 17.5 2 16 2z" fill="#111"/>
      <circle cx="16" cy="27.5" r="2.5" fill="#111"/>
    </svg>
    FEATURED COMPANY REPORT
  </div>

  <h2 class="report-title">VERDANT SYSTEMS (OTC symbol: VRDS</h2>

  <div class="report-body">
    <p>VERDANT SYSTEMS (OTC symbol: VRDS) provides end-to-end management, across multiple systems, for medicinal marijuana operations. In our opinion, investors of VRDS could see huge returns on their investment as the market recognizes the Company as a patriarch of the industry. Our research indicates that the growth in the medical marijuana industry has left many operators and dispensaries fragmented and in need of honest, competent management to provide leadership and direction. Many medicinal marijuana companies have experienced such rapid growth that they find it difficult to manage all aspects of their operation. In order to become a successful, compliant medicinal marijuana operation, management is dependent on many different systems. Those systems, if even available, are currently so fragmented and are scattered across so many sources that they are nearly impossible to manage. This is where VRDS comes in.</p>
    <p>VRDS solves the fragmentation problem by identifying tools that are important to dispensaries</p>
  </div>

  <ul class="side-nav topics">
    <li>Featured Companies</li>
    <li>Stock Market Tips</li>
    <li>Brokerage Partners</li>
  </ul>
  <ul class="side-nav legal">
    <li>Terms of Service</li>
    <li>Privacy Policy</li>
    <li>Contact Us</li>
  </ul>
</body>
</html>
```